Web Design

We need a new website for our company. We perform several functions:

1 - IT and Network Support
2 - Computer Consultancy
3 - Cloud Services
4 - Hosted Mailvane & Online Backup
5 - Internet Connections & VOIP

Examples of some of the designs we like can be seen on:
• www.brelvox.com
• www.quintaro.com

I urgently need a new website to be designed to enable me to look more professional. My competitors website is www.tdmq.co.uk

I also want to be able to look much more professional, like www.brelvox.com www.quintaro.com

I have attached how I would like the website to look

Task outline
To design a home page and another internal skeleton page for a website following our requirements specification and wireframe layout/structure

Task description
We are looking for a modern, attractive, clean design for our new website to reflect our businesses professionalism and high quality services that we offer.
• www.brelvox.com
• www.quintaro.com
We would like a design for a home page and one other skeleton subpage for our website. We have provided a wireframe image to assist, showing how we would like the layout/structure of our website to follow which also highlights where we would like specific content/features to go.
We have listed what features the site must have in the requirements section.
The final design should communicate to our users that we are a professional business that offer high quality services and that we are a company they can trust and rely on.

Look and feel
The wireframe we have attached is a representation of how we would like the layout and structure of the website to be designed. We would like to have a corporate theme to our website.

Colours
Open to interpretation by the designer, as long as the colours suit a corporate theme and give off a professional look and feel.

Requirements
The design must have the following:

General
• Home page design (Based on attached wireframe).
• Internal Page design (This needs to be a skeleton page which can be used for implemented the content for all over pages).

• Contact details to be visible on every page, contact number at the header and all other relative details in the footer section.
• Social networking icons within the footer section of the site.
• Avoid the use of unprofessional images for buttons, icons and banners etc.
Features desired
• Drop down navigation bar. Please see the attached image for inspiration for its design/layout.
o We would like a similar drop down menu design to the one on this site: www.tdmq.co.uk.
• Image slider at the header of every page just beneath the navigation bar.
o We would like the Plexa slider to be used for the image slider. Please use this link for an example of it in action: http://www.scriptloomhub.net/demo/plexa-slider/
o The image slider needs to be larger on the home page.
o The image slider can be smaller on the rest of the pages of the site.
• Chirply feed present on every page.
• News/Blog feed present on every page.
• Call back form present on every page.
• Wayfindr Map implementation above footer on every page.

A user friendly, accessible design that is easy to use and easy for the user to understand. Must have a corporate theme to reflect the professionalism of our business. Content flows logically and keep content spaced out so that it does not make the site look cluttered.

Target Market(s)

Small to Mid sized Business, Large Banks and Legal, corporate, business - non-technical users

Industry/Entity Type

Business

Font styles to use
Sans Serif

```html
<!DOCTYPE html>
<html lang="en">
<head>
<meta charset="utf-8">
<title>Clydemoor Systems — IT Support</title>
<link rel="stylesheet" href="https://fonts.googleapis.com/css2?family=Arimo:wght@400;700&display=swap">
<style>
:root{
  --brand:#2b5f8e;
  --brand-dark:#204d76;
  --brand-deep:#1d4569;
  --title:#2d6aa0;
  --text:#333;
  --muted:#666;
  --line:#cfcfcf;
  --accent:#e05a1e;
  --nav-top:#676a6f;
  --nav-bottom:#45484c;
  --btn:#54575b;
  --tick:#6aa82c;
  --white:#fff;
}
*{box-sizing:border-box;margin:0;padding:0}
html,body{width:1200px;height:2359px;overflow:hidden}
body{font-family:"Arimo",Arial,sans-serif;color:var(--text);background:var(--white);position:relative;font-size:12px}
.abs{position:absolute}
a{color:inherit;text-decoration:none}

/* header */
.site-header{position:absolute;left:0;top:0;width:1200px;height:90px;background:var(--white)}
.brand{left:184px;top:26px;font-size:28px;color:var(--brand);letter-spacing:.5px}
.header-phone{left:746px;top:38px;font-size:16px;color:#333;display:flex;align-items:center;gap:8px}
.cta{left:892px;top:34px;width:120px;height:32px;border-radius:3px;background:linear-gradient(#8dbde8,#5d96cb);color:#fff;font-size:13px;display:flex;align-items:center;justify-content:center;border:1px solid #4f88bd}

/* nav */
.main-nav{position:absolute;left:0;top:90px;width:1200px;height:41px;background:linear-gradient(var(--nav-top),var(--nav-bottom))}
.main-nav a{position:absolute;top:13px;color:#fff;font-size:13px}

/* slider */
.slider{position:absolute;left:0;top:131px;width:1200px;height:385px;background:linear-gradient(90deg,#2a2d31 0%,#6b7077 30%,#c9ccd0 50%,#6b7077 70%,#25282c 100%)}
.slider-arrow{position:absolute;top:307px;width:40px;height:40px}
.caption{position:absolute;left:184px;background:rgba(43,95,142,.85);color:#fff;padding:0 14px;display:flex;align-items:center;white-space:nowrap}
.caption-title{top:390px;height:38px;width:201px;font-size:17px}
.caption-sub{top:436px;height:37px;width:437px;font-size:15px}

/* dropdown */
.dropdown{position:absolute;left:327px;top:137px;width:397px;height:222px;background:#fff;box-shadow:0 2px 6px rgba(0,0,0,.35);padding:18px 20px 0 20px;display:flex;gap:25px}
.dropdown ul{list-style:none;width:175px}
.dropdown li{height:28.4px;line-height:26px;border-bottom:1px solid #d6d6d6;font-size:11px;color:#444}

/* main */
.section-title{font-size:15px;font-weight:400;color:var(--title)}
.rule{position:absolute;left:184px;width:562px;height:1px;background:var(--line)}
.photo{position:absolute}
.intro-text{left:414px;top:586px;width:332px;font-size:10.5px;line-height:17.5px}
.intro-text p:first-child{color:#222}
.intro-text p+p{color:var(--muted);margin-top:3px}

.service{position:absolute;width:266px}
.service h3{font-size:14px;font-weight:400;color:var(--title);margin-bottom:10px}
.service ul{list-style:none}
.service li{font-size:11px;height:26.5px;display:flex;gap:10px;align-items:flex-start;color:#444}
.btn{display:flex;align-items:center;justify-content:center;width:102px;height:29px;border-radius:3px;background:var(--btn);color:#fff;font-size:11px;margin:10px 0 0 4px}

.quote{position:absolute;top:1524px;width:266px;height:115px;background:linear-gradient(#fafafa,#ececec);border:1px solid #d8d8d8;border-radius:3px;padding:20px 30px 0 44px;font-size:10px;font-style:italic;color:#777;line-height:17px;overflow:hidden}
.quote .mark{position:absolute;font-size:30px;color:#aaa;font-style:normal;font-family:Georgia,serif;line-height:1}
.client{position:absolute;top:1648px;display:flex;gap:12px;align-items:flex-start}
.client .badge{width:56px;height:56px;border:1px solid #ccc;background:#fff;display:flex;align-items:center;justify-content:center}
.client .who{font-size:11px;line-height:19px}
.client .who b{font-weight:400;font-style:italic;color:var(--title)}

.partners{position:absolute;left:184px;top:1741px;width:832px;height:65px;border:1px solid #d0d0d0;display:flex;align-items:center;justify-content:space-around;padding:0 30px}
.partners span{font-size:18px;font-weight:700;color:#2d4d78}
.partners .edge{position:absolute;top:0;width:12px;height:63px;background:#eee;color:#999;font-size:10px;display:flex;align-items:center;justify-content:center}

/* sidebar */
.callback{position:absolute;left:783px;top:544px;width:233px;height:318px;background:var(--brand);padding:14px 14px;color:#fff;font-size:10px;text-align:center;line-height:16px}
.callback .field{background:#fff;height:26px;border-radius:2px;margin:8px 6px 0;color:#888;text-align:left;padding:5px 8px;font-size:10px}
.callback .msg{height:52px}
.callback .send{width:88px;height:28px;margin:10px 6px 0 auto;border-radius:3px;background:linear-gradient(#9cc6ec,#6a9fd1);display:flex;align-items:center;justify-content:center;font-size:12px}

.feed-head{left:785px;top:890px;display:flex;align-items:center;gap:12px}
.feed-head .name{font-size:19px;font-weight:700;color:#35a0d8}
.feed-head .sub{font-size:12px;color:#555}
.profile{position:absolute;left:785px;top:930px;width:231px;height:58px;border:1px solid #d3d3d3;display:flex;align-items:center;gap:12px;padding:0 6px;font-size:12px;color:var(--brand-dark);line-height:17px}
.profile .sq{width:68px;height:46px;background:var(--brand-dark)}
.tweet{position:absolute;left:785px;width:231px;height:86px;font-size:9.5px;line-height:17px;color:#444;border-bottom:1px solid #d3d3d3;padding-top:2px}
.tweet i{color:var(--brand)}
.tweet .url{word-break:break-all}
.tweet .meta{color:var(--brand);font-style:italic;font-weight:700;font-size:9px}
.orange{color:var(--accent);font-size:11px;position:absolute}

.news-head{position:absolute;left:785px;top:1318px;width:231px;height:35px;background:var(--btn);color:#fff;font-size:13px;padding:10px 18px}
.news{position:absolute;left:785px;width:231px;height:96px;border-bottom:1px solid #d3d3d3;display:flex;gap:12px;padding-top:10px}
.news .thumb{width:66px;height:68px;border:1px solid #bbb;flex:none}
.news .body{font-size:10px;line-height:18px;color:#444}
.news .body b{font-weight:400;color:var(--brand)}
.news .body em{font-style:normal;color:var(--accent)}

/* map */
.map{position:absolute;left:0;top:1843px;width:1200px;height:296px;background:linear-gradient(135deg,#e6e3dc,#efece6 55%,#e1ddd3)}

/* footer */
.site-footer{position:absolute;left:0;top:2139px;width:1200px;height:181px;background:var(--brand);color:#fff}
.site-footer h4{font-size:12px;font-weight:400;margin-bottom:12px}
.fcol{position:absolute;top:30px;font-size:10px;line-height:17.5px}
.social{display:flex;align-items:center;gap:8px;margin-bottom:10px}
.social i{width:26px;height:26px;border-radius:50%;background:#4a9fdc;display:block}
.copyright{position:absolute;left:0;top:2320px;width:1200px;height:39px;background:var(--brand-deep);color:#fff;font-size:10px;text-align:center;line-height:39px}
</style>
</head>
<body>

<header class="site-header">
  <div class="abs brand">Clydemoor Systems</div>
  <div class="abs header-phone">
    <svg width="18" height="18" viewBox="0 0 24 24"><path fill="#333" d="M6.6 10.8a15.1 15.1 0 0 0 6.6 6.6l2.2-2.2c.3-.3.7-.4 1-.2 1.1.4 2.3.6 3.6.6.6 0 1 .4 1 1V20c0 .6-.4 1-1 1A17 17 0 0 1 3 4c0-.6.4-1 1-1h3.5c.6 0 1 .4 1 1 0 1.3.2 2.5.6 3.6.1.3 0 .7-.2 1z"/></svg>
    0141 555 0192
  </div>
  <a class="abs cta" href="#contact">Get in Touch</a>
</header>

<nav class="main-nav">
  <a style="left:236px">Home</a>
  <a style="left:335px">Products</a>
  <a style="left:448px">Company</a>
  <a style="left:566px">Blog</a>
</nav>

<section class="slider" role="img" aria-label="Slider photo: long corridor of server racks in a data centre"></section>
<svg class="slider-arrow" style="left:77px" viewBox="0 0 40 40"><circle cx="20" cy="20" r="18" fill="rgba(0,0,0,.35)" stroke="rgba(255,255,255,.5)" stroke-width="2"/><path d="M23 12l-8 8 8 8" fill="none" stroke="rgba(255,255,255,.7)" stroke-width="3"/></svg>
<svg class="slider-arrow" style="left:1079px" viewBox="0 0 40 40"><circle cx="20" cy="20" r="18" fill="rgba(0,0,0,.35)" stroke="rgba(255,255,255,.5)" stroke-width="2"/><path d="M17 12l8 8-8 8" fill="none" stroke="rgba(255,255,255,.7)" stroke-width="3"/></svg>
<div class="caption caption-title">Clyde Moor Systems</div>
<div class="caption caption-sub">Worldwide Coverage, Vantoria Professionals 24 hours a day</div>

<div class="dropdown">
  <ul>
    <li>Services</li><li>Business Solutions</li><li>Backup and Recovery</li><li>Broadband</li><li>Consultancy Planning</li><li>Email</li><li style="border:0">Free Audit</li>
  </ul>
  <ul>
    <li>Implementation Services</li><li>Mobile Office</li><li>Network Design</li><li>Procurement</li><li>Server Platforms</li><li>TeamVault</li><li style="border:0">Virtualisation</li>
  </ul>
</div>

<!-- welcome -->
<h2 class="abs section-title" style="left:184px;top:547px">Welcome to Clyde Moor Systems</h2>
<div class="photo" style="left:184px;top:590px;width:212px;height:146px;background:linear-gradient(120deg,#d9e2ea,#9fb3c6)" role="img" aria-label="Photo of a smiling businessman giving a thumbs up"></div>
<div class="abs intro-text">
  <p>For many companies today, IT support is a large part of doing business. It is not always possible for a company or business to have a dedicated IT support team. For companies/businesses in Glasgow, Scotland, the answer for IT needs is Clydemoor Systems Limited</p>
  <p>With Clydemoor Systems Limited, a client has the full expertise of a highly skilled team of network and infrastructure engineers to monitor and manage their network. Not only do the IT consultants of Clydemoor Systems Limited troubleshoot issues...</p>
</div>
<div class="rule" style="top:766px"></div>

<!-- services -->
<div class="photo" style="left:184px;top:791px;width:266px;height:150px;background:linear-gradient(135deg,#3d3f42,#6b6e70 55%,#3fae3a 56%,#2e8a2b)" role="img" aria-label="Photo of a keyboard with a green Backup key"></div>
<div class="photo" style="left:480px;top:791px;width:266px;height:150px;background:linear-gradient(135deg,#2c3e55,#8fb2d1 60%,#e3ecf3)" role="img" aria-label="Photo of two engineers with a laptop in a server room"></div>
<div class="photo" style="left:184px;top:1133px;width:266px;height:150px;background:linear-gradient(135deg,#0f4f8a,#3d9ad6 55%,#bfe0f5)" role="img" aria-label="Illustration of a woman touching a digital interface"></div>
<div class="photo" style="left:480px;top:1133px;width:266px;height:150px;background:linear-gradient(90deg,#2a2d31,#a8acb1 50%,#2a2d31)" role="img" aria-label="Photo of a data centre aisle"></div>

<div class="service" style="left:184px;top:958px">
  <h3>Online Backup</h3>
  <ul>
    <li><svg width="12" height="12" viewBox="0 0 12 12"><path d="M1 6l3.5 3.5L11 2" fill="none" stroke="#6aa82c" stroke-width="2.4"/></svg>Protect your valuable data securely offsite.</li>
    <li><svg width="12" height="12" viewBox="0 0 12 12"><path d="M1 6l3.5 3.5L11 2" fill="none" stroke="#6aa82c" stroke-width="2.4"/></svg>Instant Recovery.</li>
    <li><svg width="12" height="12" viewBox="0 0 12 12"><path d="M1 6l3.5 3.5L11 2" fill="none" stroke="#6aa82c" stroke-width="2.4"/></svg>Unlimited Data Plans Available.</li>
  </ul>
  <a class="btn">Find out more</a>
</div>
<div class="service" style="left:480px;top:958px">
  <h3>Onsite It Support</h3>
  <ul>
    <li><svg width="12" height="12" viewBox="0 0 12 12"><path d="M1 6l3.5 3.5L11 2" fill="none" stroke="#6aa82c" stroke-width="2.4"/></svg>No Travel or Call Out Charge.</li>
    <li><svg width="12" height="12" viewBox="0 0 12 12"><path d="M1 6l3.5 3.5L11 2" fill="none" stroke="#6aa82c" stroke-width="2.4"/></svg>Vantoria and Polmont Engineers 24*7.</li>
    <li><svg width="12" height="12" viewBox="0 0 12 12"><path d="M1 6l3.5 3.5L11 2" fill="none" stroke="#6aa82c" stroke-width="2.4"/></svg>Fixed Cost Repairs.</li>
  </ul>
  <a class="btn">Find out more</a>
</div>
<div class="service" style="left:184px;top:1299px">
  <h3>Remote It Support</h3>
  <ul>
    <li><svg width="12" height="12" viewBox="0 0 12 12"><path d="M1 6l3.5 3.5L11 2" fill="none" stroke="#6aa82c" stroke-width="2.4"/></svg>Anyplace, Anytime - we fix YOUR issues.</li>
    <li><svg width="12" height="12" viewBox="0 0 12 12"><path d="M1 6l3.5 3.5L11 2" fill="none" stroke="#6aa82c" stroke-width="2.4"/></svg>Experts on-call 24*7.</li>
    <li><svg width="12" height="12" viewBox="0 0 12 12"><path d="M1 6l3.5 3.5L11 2" fill="none" stroke="#6aa82c" stroke-width="2.4"/></svg>Fixed Costs.</li>
  </ul>
  <a class="btn">Find out more</a>
</div>
<div class="service" style="left:480px;top:1299px">
  <h3>Hosted Mailvane</h3>
  <ul>
    <li><svg width="12" height="12" viewBox="0 0 12 12"><path d="M1 6l3.5 3.5L11 2" fill="none" stroke="#6aa82c" stroke-width="2.4"/></svg>Throw out your Email server!</li>
    <li><svg width="12" height="12" viewBox="0 0 12 12"><path d="M1 6l3.5 3.5L11 2" fill="none" stroke="#6aa82c" stroke-width="2.4"/></svg>Let Us Manage your Email!</li>
    <li><svg width="12" height="12" viewBox="0 0 12 12"><path d="M1 6l3.5 3.5L11 2" fill="none" stroke="#6aa82c" stroke-width="2.4"/></svg>Plans from £5.95 a month.</li>
  </ul>
  <a class="btn">Find out more</a>
</div>

<div class="rule" style="top:1469px"></div>

<!-- testimonials -->
<h2 class="abs section-title" style="left:184px;top:1488px">What Our Clients Say's</h2>
<svg class="abs" style="left:722px;top:1493px" width="24" height="12" viewBox="0 0 24 12"><path d="M6 2l-4 4 4 4M18 2l4 4-4 4" fill="none" stroke="#aaa" stroke-width="1.6"/></svg>
<div class="quote" style="left:184px"><span class="mark" style="left:14px;top:14px">&#8220;</span>We have used Clydemoor Systems Ltd for many IT services across a number of companies that I have been involved with. They are dedicated professionals...<span class="mark" style="right:14px;bottom:10px">&#8221;</span></div>
<div class="quote" style="left:480px"><span class="mark" style="left:14px;top:14px">&#8220;</span>We have used Clydemoor Systems Ltd for many IT services across a number of companies that I have been involved with. They are dedicated professionals...<span class="mark" style="right:14px;bottom:10px">&#8221;</span></div>
<div class="client" style="left:184px"><div class="badge"><svg width="34" height="34"><rect width="34" height="34" fill="#c43b2e"/></svg></div><div class="who"><b>Alasdair Finlay</b><br>Tarnbrook Fabrication</div></div>
<div class="client" style="left:480px"><div class="badge"><svg width="34" height="34"><rect width="34" height="34" fill="#3c7a4a"/></svg></div><div class="who"><b>Ewan M</b><br>Lowland Ventures</div></div>

<div class="partners">
  <div class="edge" style="left:0">&lsaquo;</div>
  <span>Corvane</span><span>Nexbyte</span><span>Hollin</span><span>Veridane</span><span>Keystrand</span><span>Polmont</span><span>Halvern</span>
  <div class="edge" style="right:0">&rsaquo;</div>
</div>

<!-- sidebar -->
<aside class="callback" id="contact">
  <p>We guarantee to respond within one hour<br>Alternatively call us on: 0141 555 0192<br>See more at: http://www.clydemoor-systems.com/#sthash.4ScVInsy.dpuf</p>
  <div style="margin-top:12px">
    <div class="field">Name :</div>
    <div class="field">Email :</div>
    <div class="field">Phone :</div>
    <div class="field msg">Message :</div>
    <div class="send">Send</div>
  </div>
</aside>

<div class="abs feed-head"><span class="name">Chirply</span><span class="sub">Feeds</span></div>
<div class="profile"><div class="sq"></div><div>Clydemoor Systems<br><span style="color:#444">clydemoor_IT</span></div></div>
<div class="tweet" style="top:994px"><i>clydemoor_IT</i> Exciting news: we are expanding into southern ireland! - See more at: <i class="url">http://www.clydemoor-systems.com/#sthash.4ScVInsy.dpuf</i><br><span class="meta">6 months . reply . retweet . favorite</span></div>
<div class="tweet" style="top:1088px"><i>clydemoor_IT</i> Exciting news: we are expanding into southern ireland! - See more at: <i class="url">http://www.clydemoor-systems.com/#sthash.4ScVInsy.dpuf</i><br><span class="meta">6 months . reply . retweet . favorite</span></div>
<div class="tweet" style="top:1182px"><i>clydemoor_IT</i> Exciting news: we are expanding into southern ireland! - See more at: <i class="url">http://www.clydemoor-systems.com/#sthash.4ScVInsy.dpuf</i><br><span class="meta">6 months . reply . retweet . favorite</span></div>
<span class="orange" style="left:908px;top:1282px">[ join the conversation ]</span>

<div class="news-head">Latest News</div>
<div class="news" style="top:1362px"><div class="thumb" style="background:linear-gradient(135deg,#555,#bbb)" role="img" aria-label="Photo of hands typing on a laptop"></div><div class="body"><b>Why Our Competitors Hate Us....</b><br>When you hire IT Consultants from us, we give you...<br><em>[ Read more ]</em></div></div>
<div class="news" style="top:1458px"><div class="thumb" style="background:linear-gradient(135deg,#6d5a4a,#c9b8a6)" role="img" aria-label="Photo of a hand holding a phone"></div><div class="body"><b>Why Our Competitors Hate Us....</b><br>When you hire IT Consultants from us, we give you...<br><em>[ Read more ]</em></div></div>
<div class="news" style="top:1554px"><div class="thumb" style="background:linear-gradient(135deg,#7e93a8,#dfe5ea)" role="img" aria-label="Photo of a senior businessman"></div><div class="body"><b>Why Our Competitors Hate Us....</b><br>When you hire IT Consultants from us, we give you...<br><em>[ Read more ]</em></div></div>
<span class="orange" style="left:941px;top:1660px">[ See All News ]</span>

<!-- map -->
<section class="map" role="img" aria-label="Street map with a pin marking the office at 14-16 Harbour Lane"></section>

<!-- footer -->
<footer class="site-footer">
  <div class="fcol" style="left:228px"><h4>CONTACT INFORMATION</h4>Clydemoor Systems Limited<br>14-16 Harbour Lane, Kelburn,<br>KL9 4TQ<br>Phone : +44(0)141 5550192<br>Email : uk.info@clydemoor-systems.com</div>
  <div class="fcol" style="left:451px"><h4>Navigation</h4>Home<br>Company<br>IT Support<br>Cloud Services<br>Partners</div>
  <div class="fcol" style="left:566px;top:59px">Contact Us<br>News<br>Terms &amp; Conditions<br>Sitemap</div>
  <div class="fcol" style="left:702px"><h4>IT Support</h4>IT Support Glasgow<br>IT Support Edinburgh<br>IT Support Perth<br>IT Support Stirling<br>IT Support Paisley</div>
  <div class="fcol" style="left:846px"><h4>Follow us :</h4>
    <div class="social"><i></i>: Friendloop</div>
    <div class="social"><i></i>: Chirply</div>
    <div class="social"><i></i>: Workweave</div>
  </div>
</footer>
<div class="copyright">Copyrights © Clyde Moor Systems 2014. All rights reserved.</div>

</body>
</html>
```